Political Mail Out Quintero front and back

Front
Esteban (9th Grade) Quintero!

What's that famous saying?

Show me who your friends are and I'll tell you who you really are!
(show the two guys)

Walter Cuellar is charged with voter fraud by changing voter addresses from across the RGV so they could vote in Edinburg
Back
Did Esteban (9th Grade) Quintero commit voter fraud when he ran for office in 2016?
(insert blurred photo)

Here is a list of people from all over the RGV that voted in Edinburg in the 2016 race.
Here is a break down:

(highlight the number and where they were first registered to vote)

9 People voted in Edinburg who were registered in Donna.
13 People voted in Edinburg who were registered in San Juan
8 People voted in Edinburg who were registered in Pharr
31 People voted in Edinburg who were registered in McAllen
2 People voted in Edinburg who were registered in La Joya
6 People voted in Edinburg who were registered in Edcouch
2 People voted in Edinburg who were registered in Mercedes
2 People voted in Edinburg who were registered in Monte Alto
6 People voted in Edinburg who were registered in Weslaco
1 Person voted in Edinburg who were registered in Penitas
3 People voted in Edinburg who were registered in Alamo
5 People voted in Edinburg who were registered in Elsa
6 People voted in Edinburg who were registered in Mission
1 Person voted in Edinburg who were registered in Alton

Will Esteban (9th Grade) Quintero CHEAT in 2020?

Only time will tell.

Vote Esteban (9th Grade) Quintero OUT of office.

```html
<!DOCTYPE html>
<html lang="en">
<head>
<meta charset="utf-8">
<title>Quintero Mail Out – Front and Back</title>
<link href="https://fonts.googleapis.com/css2?family=Cinzel:wght@600;700&family=Lato:wght@400;700;900&display=swap" rel="stylesheet">
<style>
  :root {
    --navy: #1d4587;
    --red: #c9262b;
    --ink: #1c1c1c;
    --grey-text: #3a3a3a;
    --rule: #b5b5b5;
    --panel: #f6f6f6;
    --paper: #ffffff;
    --backdrop: #eeebe5;
  }
  * { box-sizing: border-box; margin: 0; padding: 0; }
  html, body { width: 1200px; height: 1200px; overflow: hidden; background: var(--backdrop); }
  body { position: relative; font-family: "Lato", Arial, sans-serif; color: var(--ink); }

  .card { position: absolute; left: 210px; width: 780px; height: 520px; background: var(--navy); }
  .card--front { top: 50px; }
  .card--back { top: 620px; }
  .card__inner { position: absolute; left: 25px; top: 26px; width: 729px; height: 468px; background: var(--paper); }
  .abs { position: absolute; }

  /* Front */
  .front__kicker { left: 58px; top: 66px; font-size: 16px; color: var(--ink); }
  .front__headline { left: 56px; top: 92px; font-family: "Cinzel", Georgia, serif; font-weight: 700; font-size: 58px; line-height: 54px; letter-spacing: 0.5px; }
  .front__headline span { display: block; }
  .front__headline .blue { color: var(--navy); }
  .front__headline .red { color: var(--red); }
  .divider { height: 1px; background: var(--rule); }
  .divider::before { content: ""; position: absolute; left: 0; top: -2px; width: 30px; height: 5px; border-radius: 3px; background: var(--navy); }
  .front__divider { left: 58px; top: 327px; width: 257px; }
  .front__saying { left: 58px; top: 344px; width: 270px; font-size: 16.5px; font-weight: 700; line-height: 19.5px; text-transform: uppercase; }
  .front__charge { left: 58px; top: 414px; width: 265px; font-size: 12.2px; line-height: 15.5px; color: var(--grey-text); }
  .photo { position: absolute; }
  .photo--friend-one { left: 373px; top: 121px; width: 186px; height: 250px; background: linear-gradient(160deg, #e7e3dc, #b9a89a 60%, #8c7a6e); }
  .photo--building { left: 373px; top: 371px; width: 186px; height: 123px; background: linear-gradient(180deg, #b3262a, #d9352f 70%, #a01f22); }
  .photo--sky { left: 566px; top: 26px; width: 188px; height: 72px; background: linear-gradient(135deg, #1c2f6e, #3a5aa8); }
  .photo--friend-two { left: 566px; top: 98px; width: 188px; height: 248px; background: linear-gradient(170deg, #7a5a3a, #8a7a6c 45%, #6f6f6f); }
  .front__web { left: 591px; top: 413px; font-size: 14.5px; letter-spacing: 1.6px; color: var(--red); }

  /* Back */
  .back__panel { left: 25px; top: 26px; width: 365px; height: 468px; background: var(--panel); }
  .back__title { left: 46px; top: 37px; width: 330px; font-family: "Cinzel", Georgia, serif; font-weight: 600; font-size: 18.5px; line-height: 18px; color: var(--red); }
  .back__divider { left: 46px; top: 101px; width: 308px; }
  .back__intro { left: 46px; top: 112px; width: 320px; font-size: 10.5px; line-height: 13px; color: var(--grey-text); }
  .back__intro strong { font-weight: 700; color: var(--ink); }
  .tally { left: 46px; top: 160px; list-style: none; font-size: 10.5px; line-height: 14.45px; color: var(--grey-text); }
  .tally .count { color: var(--red); font-weight: 700; }
  .tally .town { color: var(--navy); }
  .back__question { left: 25px; top: 374px; width: 365px; height: 51px; background: var(--navy); padding: 4px 0 0 22px; font-family: "Cinzel", Georgia, serif; font-weight: 600; font-size: 19.5px; line-height: 20px; color: #fff; }
  .back__answer { left: 25px; top: 428px; width: 365px; text-align: center; font-family: "Cinzel", Georgia, serif; font-weight: 600; font-size: 19.5px; color: var(--red); }
  .back__call { left: 25px; top: 455px; width: 365px; text-align: center; font-size: 10px; text-transform: uppercase; color: var(--ink); }
  .back__footer { left: 25px; top: 476px; width: 365px; height: 18px; background: var(--red); color: #fff; font-size: 10px; letter-spacing: 1.2px; text-align: center; line-height: 18px; }
  .stamp-box { left: 659px; top: 57px; width: 61px; height: 69px; border: 1px solid var(--red); }
  .address-line { left: 434px; width: 286px; height: 1px; background: var(--red); }
</style>
</head>
<body>

<section class="card card--front" aria-label="Mail out front">
  <div class="card__inner"></div>
  <p class="abs front__kicker">Esteban (9th Grade) Quintero!</p>
  <h1 class="abs front__headline">
    <span class="blue">What's</span>
    <span class="red">That</span>
    <span class="blue">Famous</span>
    <span class="red">Saying?</span>
  </h1>
  <div class="abs divider front__divider"></div>
  <p class="abs front__saying">Show me who your friends are and I'll tell you who you really are!</p>
  <p class="abs front__charge">Walter Cuellar is charged with voter fraud by changing voter addresses from across the RGV so they could vote in Edinburg</p>
  <div class="photo photo--friend-one" role="img" aria-label="Photo of the first friend smiling in a white campaign shirt"></div>
  <div class="photo photo--building" role="img" aria-label="Red-toned photo of a building entrance"></div>
  <div class="photo photo--sky" role="img" aria-label="Blue-toned photo of an office building at dusk"></div>
  <div class="photo photo--friend-two" role="img" aria-label="Photo of the second friend smiling in a grey campaign shirt"></div>
  <p class="abs front__web">www.website.com</p>
</section>

<section class="card card--back" aria-label="Mail out back">
  <div class="card__inner"></div>
  <div class="abs back__panel"></div>
  <h2 class="abs back__title">Did Esteban (9th Grade) Quintero commit voter fraud when he ran for office in 2016?</h2>
  <div class="abs divider back__divider"></div>
  <p class="abs back__intro">Here is a list of people from all over the RGV that voted in Edinburg in the 2016 race.<br><strong>Here is a break down:</strong></p>
  <ul class="abs tally">
    <li><span class="count">9 People voted</span> in Edinburg who were registered <span class="town">in Donna</span>.</li>
    <li><span class="count">13 People voted</span> in Edinburg who were registered <span class="town">in San Juan</span></li>
    <li><span class="count">8 People voted</span> in Edinburg who were registered <span class="town">in Pharr</span></li>
    <li><span class="count">31 People voted</span> in Edinburg who were registered <span class="town">in McAllen</span></li>
    <li><span class="count">2 People voted</span> in Edinburg who were registered <span class="town">in La Joya</span></li>
    <li><span class="count">6 People voted</span> in Edinburg who were registered <span class="town">in Edcouch</span></li>
    <li><span class="count">2 People voted</span> in Edinburg who were registered <span class="town">in Mercedes</span></li>
    <li><span class="count">2 People voted</span> in Edinburg who were registered <span class="town">in Monte Alto</span></li>
    <li><span class="count">6 People voted</span> in Edinburg who were registered <span class="town">in Weslaco</span></li>
    <li><span class="count">1 Person voted</span> in Edinburg who were registered <span class="town">in Penitas</span></li>
    <li><span class="count">3 People voted</span> in Edinburg who were registered <span class="town">in Alamo</span></li>
    <li><span class="count">5 People voted</span> in Edinburg who were registered <span class="town">in Elsa</span></li>
    <li><span class="count">6 People voted</span> in Edinburg who were registered <span class="town">in Mission</span></li>
    <li><span class="count">1 Person voted</span> in Edinburg who were registered <span class="town">in Alton</span></li>
  </ul>
  <p class="abs back__question">Will Esteban (9th Grade)<br>Quintero CHEAT in 2020?</p>
  <p class="abs back__answer">Only time will tell.</p>
  <p class="abs back__call">Vote Esteban (9th Grade) Quintero out of office.</p>
  <p class="abs back__footer">www.website.com</p>
  <div class="abs stamp-box"></div>
  <div class="abs address-line" style="top:194px"></div>
  <div class="abs address-line" style="top:268px"></div>
  <div class="abs address-line" style="top:342px"></div>
  <div class="abs address-line" style="top:416px"></div>
</section>

</body>
</html>
```